Marisol Trevenko - Business Card Design

Hello everyone,

I need business cards designed to the following specs:

3.5"x2" with .25" bleed all around for printing
Square corners only

Please use attached business card for design reference.

Front:

Marisol Trevenko
Broker Associate

305-742-1186
marisoltrevenko@ quillmail.com (no space)
Instagram Logo @mtrevko
Facebook Logo Marisol Trevenko
4812 NW 127th St, Ste #210
Miami, Lakes, FL 33027

Back:

Brightway logo

Please submit editable AI, PDF, and JPG files.

Thanks and good luck!!!

```html
<!DOCTYPE html>
<html lang="en">
<head>
<meta charset="utf-8">
<title>Marisol Trevenko – Business Card</title>
<link href="https://fonts.googleapis.com/css2?family=Montserrat:wght@400;500;700;800&display=swap" rel="stylesheet">
<style>
  :root {
    --stage: #2a566d;
    --card: #0b0b0c;
    --card-edge: #1a1a1c;
    --ink: #f2f2f2;
    --ink-soft: #cfcfcf;
    --accent: #e0252d;
  }
  * { margin: 0; padding: 0; box-sizing: border-box; }
  html, body {
    width: 1200px; height: 885px; overflow: hidden;
    background: var(--stage);
    font-family: "Montserrat", Arial, sans-serif;
    color: var(--ink);
  }
  .canvas { position: relative; width: 1200px; height: 885px; }

  .card {
    position: absolute; left: 250px; width: 700px; height: 400px;
    background: var(--card);
    border: 1px solid var(--card-edge);
    overflow: hidden;
  }
  .card--back { top: 30px; }
  .card--front { top: 455px; }

  /* Back: brand */
  .brand {
    position: absolute; inset: 0;
    display: flex; align-items: center; justify-content: center;
  }
  .brand__name {
    font-weight: 700; font-size: 62px; letter-spacing: 6px;
    text-transform: uppercase; color: var(--ink);
  }

  /* Front */
  .portrait {
    position: absolute; left: 430px; top: 28px; width: 240px; height: 220px;
    background: radial-gradient(ellipse at 50% 40%, #c9a27f 0%, #8a6a55 35%, #3a2c28 70%, #111 100%);
  }
  .divider {
    position: absolute; left: 402px; top: 118px; width: 2px; height: 150px;
    background: var(--accent);
  }
  .edge-marks { position: absolute; left: 0; top: 250px; width: 26px; }
  .edge-marks span {
    display: block; height: 3px; background: var(--accent); margin-bottom: 7px;
  }

  .identity { position: absolute; left: 48px; top: 118px; }
  .identity__name {
    font-weight: 800; font-size: 24px; letter-spacing: 1px;
    color: var(--accent); text-transform: uppercase;
  }
  .identity__role { font-size: 16px; font-weight: 500; margin-top: 4px; }

  .address {
    position: absolute; left: 48px; top: 190px;
    font-size: 15px; line-height: 1.45; color: var(--ink);
  }
  .contact { position: absolute; left: 48px; top: 246px; font-size: 15px; }
  .contact__row { display: flex; align-items: center; gap: 9px; height: 24px; }
  .contact__icon {
    width: 18px; height: 18px; border-radius: 50%; background: var(--accent);
    display: flex; align-items: center; justify-content: center; flex: none;
  }

  .social {
    position: absolute; top: 318px; display: flex; flex-direction: column;
    align-items: center; gap: 8px; font-size: 15px;
  }
  .social--one { left: 120px; }
  .social--two { left: 330px; }
  .social__dot { width: 18px; height: 18px; border-radius: 50%; background: var(--accent); }
</style>
</head>
<body>
<div class="canvas">

  <section class="card card--back" aria-label="Card back">
    <div class="brand"><span class="brand__name">Brightway</span></div>
  </section>

  <section class="card card--front" aria-label="Card front">
    <div class="portrait" role="img" aria-label="Portrait photo of Marisol Trevenko"></div>
    <div class="divider"></div>
    <div class="edge-marks"><span></span><span></span><span></span><span></span></div>

    <div class="identity">
      <div class="identity__name">Marisol Trevenko</div>
      <div class="identity__role">Broker Associate</div>
    </div>

    <div class="address">
      4812 NW 127th St, Ste #210<br>
      Miami, Lakes, FL 33027
    </div>

    <div class="contact">
      <div class="contact__row">
        <span class="contact__icon">
          <svg width="10" height="10" viewBox="0 0 10 10"><path d="M2 1 L4 1 L4.6 3 L3.5 3.8 Q4.5 5.6 6.2 6.5 L7 5.4 L9 6 L9 8 Q5 9 2.5 6 Q1 4 2 1Z" fill="#fff"/></svg>
        </span>
        <span>305-742-1186</span>
      </div>
      <div class="contact__row">
        <span class="contact__icon">
          <svg width="10" height="8" viewBox="0 0 10 8"><rect x="0.5" y="0.5" width="9" height="7" fill="none" stroke="#fff"/><path d="M0.5 0.8 L5 4.5 L9.5 0.8" fill="none" stroke="#fff"/></svg>
        </span>
        <span>marisoltrevenko@quillmail.com</span>
      </div>
    </div>

    <div class="social social--one">
      <span class="social__dot"></span>
      <span>@mtrevko</span>
    </div>
    <div class="social social--two">
      <span class="social__dot"></span>
      <span>Marisol Trevenko</span>
    </div>
  </section>

</div>
</body>
</html>
```